Medical Centre Trifold Brochure

New Medical Centre needs a bright and airy Trifold brochure. We want to introduce our practice to the surrounding area so want to advise our services and introduce the Doctors and Nurses.

I will upload all the pictures and logos, along with some pdf pages of styles that we like (and some we dont) to assist your creativity.

We will provide as much feedback for you as possible.

After this project, we would like to work with the same designer to expand into some other brochures etc that we have in mind, so this is a starting point.
Updates

Hi Designers,

We are looking forward to seeing yuor work. Are you happy that you have enough information to get started?

Please let me know if you need anything else?

Cheers

Hi Designers.. I should mention the brochure itself.. we are looking for a doubled sided, full colour brochure that will be folded into thirds so it becomes a DL size.. I hope that makes sense.

Any questions always welcome.

Target Market(s)

Females - Mothers / Wives / Grandmothers

Industry/Entity Type

Medical

Requirements
Must have
• Tri Fold Medical – Tallowby Family Health

• Include images of the Doctors (I will supply) and the Nursing Staff

• “Chunks” of information
o Introduction to who we are (I will supply)
o Our services (I will supply)
o Fee’s
• We are a newly renovated Medical Clinic
• Google Map of our location – Photo of the outside of the centre near the google map
• Opening Hours
• Contact Details / website address www.tallowbyfamilyhealth.com.au (not yet live but must be included)
• Interior Reception area photo
• Ask a question.. “Are you worried about your patient history?.. We can help”
• Need to leave a space for a Magnet.. (business card sized)

3 Doctor Photos (2 uploaded already)
Image of the centre (uploaded already)

I will upload a detailed description of what we are looking for.
Nice to have
• Photo's of 2 Nurses (1 already uploaded - Maren)

```html
<!DOCTYPE html>
<html lang="en">
<head>
<meta charset="utf-8">
<title>Tallowby Family Health – Trifold Brochure</title>
<link href="https://fonts.googleapis.com/css2?family=Questrial&family=Arimo:wght@400;700&display=swap" rel="stylesheet">
<style>
  :root {
    --lime: #8dc63f;
    --lime-light: #c4dc3a;
    --lime-dark: #5fa22c;
    --ink: #3d3d3d;
    --ink-soft: #6b6b6b;
    --paper: #ffffff;
    --stage: #e9ebe6;
    --photo-warm: #d9c7b4;
    --photo-cool: #c9d6de;
  }
  * { box-sizing: border-box; margin: 0; padding: 0; }
  html, body { width: 900px; height: 1200px; overflow: hidden; }
  body {
    background: var(--stage);
    font-family: "Arimo", Arial, sans-serif;
    color: var(--ink);
    position: relative;
  }
  .sheet {
    position: absolute;
    left: 60px;
    width: 780px;
    height: 540px;
    background: var(--paper);
    overflow: hidden;
    box-shadow: 0 2px 8px rgba(0,0,0,.12);
  }
  .sheet--outside { top: 45px; }
  .sheet--inside { top: 615px; }
  .abs { position: absolute; }
  .wave { position: absolute; left: 0; top: 0; width: 780px; }
  .heading {
    font-family: "Questrial", "Century Gothic", sans-serif;
    color: var(--ink);
    font-weight: 400;
  }

  /* Team panel */
  .team-title { left: 25px; top: 70px; font-size: 22px; }
  .member { position: absolute; left: 0; width: 258px; height: 110px; }
  .member__photo {
    position: absolute; left: 20px; top: 12px;
    width: 82px; height: 82px; border-radius: 50%;
    border: 5px solid var(--lime);
    background: radial-gradient(circle at 50% 40%, var(--photo-warm), #8c7f74);
    z-index: 2;
  }
  .member__name {
    position: absolute; left: 120px; top: -6px;
    font-family: "Questrial", sans-serif; font-size: 17px;
    line-height: 20px; white-space: nowrap;
  }
  .member__bio {
    position: absolute; left: 96px; top: 18px;
    width: 148px; height: 70px;
    background: var(--lime-light);
    border-radius: 0 14px 14px 0;
    padding: 8px 10px 6px 24px;
    font-size: 7.5px; line-height: 1.35; color: #fff;
    overflow: hidden;
  }

  /* Centre panel */
  .building {
    left: 258px; top: 22px; width: 262px; height: 124px;
    background: linear-gradient(180deg, #dfe6ea 0%, #c9a79a 55%, #8e7468 100%);
  }
  .hours-title { left: 290px; top: 180px; font-size: 21px; }
  .hours { left: 290px; top: 216px; font-size: 11.5px; line-height: 1.5; }
  .position-title { left: 290px; top: 258px; font-size: 21px; }
  .map {
    left: 290px; top: 292px; width: 168px; height: 104px;
    border: 3px solid var(--lime);
    background: linear-gradient(135deg, #eeeae2, #dcd8cf);
  }
  .contact { left: 290px; top: 412px; font-size: 10px; line-height: 1.45; color: var(--ink-soft); }
  .contact p + p.gap { margin-top: 12px; }

  /* Brand */
  .brand { left: 600px; top: 112px; display: flex; align-items: center; gap: 8px; }
  .brand__mark { width: 22px; height: 22px; background: var(--lime); }
  .brand__name {
    font-family: "Questrial", sans-serif; font-size: 17px; line-height: 1.15;
    color: var(--lime-dark); width: 130px;
  }
  .family-photo {
    left: 490px; top: 300px; width: 300px; height: 250px;
    background: linear-gradient(160deg, #f1e4d6, #d7b59b 60%, #b48c70);
    border-top-left-radius: 140px 110px;
  }

  /* Inside */
  .bubble {
    position: absolute; border-radius: 50%;
    border: 5px solid var(--lime);
    background: radial-gradient(circle at 50% 40%, #f3d8c4, #c58b6a);
  }
  .dot { position: absolute; border-radius: 50%; background: var(--lime); }
  .dot--ring { background: transparent; border: 4px solid var(--lime-light); }
  .col { position: absolute; width: 184px; }
  .col h2 { font-family: "Questrial", sans-serif; font-weight: 400; font-size: 25px; margin-bottom: 12px; }
  .col .lead { font-weight: 700; font-size: 11px; line-height: 1.3; margin-bottom: 12px; }
  .col .body { font-size: 11px; line-height: 1.3; color: var(--ink-soft); text-align: justify; }
  .col--about { left: 42px; top: 105px; }
  .col--services { left: 297px; top: 160px; }
  .col--fees { left: 577px; top: 152px; width: 180px; }
  .services-list { list-style: none; margin-top: 14px; font-size: 11px; line-height: 1.32; color: var(--ink-soft); }
  .services-list li { position: relative; padding-left: 20px; }
  .services-list li::before {
    content: ""; position: absolute; left: 2px; top: 3px;
    width: 8px; height: 8px; border-radius: 50%; background: var(--lime);
  }
  .staff-photo { left: 0; top: 380px; width: 258px; height: 170px; background: linear-gradient(180deg, #f4f6f7, #dfe8ee 60%, #9fb3c4); }
  .group-photo { left: 278px; top: 430px; width: 240px; height: 120px; background: linear-gradient(180deg, #f6ece2, #d8b79d); }
  .couple-photo { left: 592px; top: 410px; width: 188px; height: 140px; background: linear-gradient(180deg, #f1ebe4, #c9b3a3 70%, #8f8f9c); }
</style>
</head>
<body>

<section class="sheet sheet--outside">
  <svg class="wave" height="90" viewBox="0 0 780 90" aria-hidden="true">
    <path d="M0 0 H780 V30 C620 70 460 10 300 35 C180 52 80 40 0 30 Z" fill="var(--lime)"/>
    <path d="M0 30 C80 40 180 52 300 35 C460 10 620 70 780 30 V44 C620 82 460 22 300 46 C180 62 80 50 0 40 Z" fill="var(--lime-light)"/>
  </svg>

  <h1 class="abs heading team-title">Our Team</h1>

  <div class="member" style="top:135px">
    <div class="member__photo" role="img" aria-label="Portrait photo of Dr. Elena"></div>
    <div class="member__name">Dr. Elena</div>
    <p class="member__bio">Family doctor with a warm approach, caring for children, parents and grandparents across the local community for many years.</p>
  </div>
  <div class="member" style="top:263px">
    <div class="member__photo" role="img" aria-label="Portrait photo of Dr. Maren"></div>
    <div class="member__name">Dr. Maren</div>
    <p class="member__bio">General practitioner with a keen interest in women's health, antenatal care and supporting new mothers through every stage.</p>
  </div>
  <div class="member" style="top:391px">
    <div class="member__photo" role="img" aria-label="Portrait photo of Dr. Owen Hartley"></div>
    <div class="member__name">Dr. Owen Hartley</div>
    <p class="member__bio">Experienced GP focused on men's health, chronic disease care and sports injuries, helping patients stay active and well.</p>
  </div>

  <div class="abs building" role="img" aria-label="Photo of the medical centre building exterior"></div>

  <h2 class="abs heading hours-title">Opening Hour</h2>
  <div class="abs hours">
    <p>Mon - Fri : 08.00AM - 08.00PM</p>
    <p>Sat - Sun : 10.00AM - 10.30PM</p>
  </div>

  <h2 class="abs heading position-title">POSITION</h2>
  <div class="abs map" role="img" aria-label="Street map showing the clinic location"></div>

  <div class="abs contact">
    <p>4/ 118 Fernbrook Rd, Tallowby</p>
    <p>SA 5190, Australia</p>
    <p class="gap">P : (08) 7010 2231 &nbsp; F : (08) 7010 2232</p>
    <p>info@tallowbyfamilyhealth.com.au</p>
    <p>www.tallowbyfamilyhealth.com.au</p>
  </div>

  <svg class="abs" style="left:440px;top:270px" width="340" height="280" viewBox="0 0 340 280" aria-hidden="true">
    <path d="M340 0 C200 10 80 60 40 160 C20 210 30 250 50 280 H340 Z" fill="var(--lime)"/>
  </svg>
  <div class="abs brand">
    <span class="brand__mark"></span>
    <span class="brand__name">Tallowby Family Health</span>
  </div>
  <div class="abs family-photo" role="img" aria-label="Photo of a smiling family of four"></div>
</section>

<section class="sheet sheet--inside">
  <svg class="wave" height="90" viewBox="0 0 780 90" aria-hidden="true">
    <path d="M0 0 H780 V40 C640 70 520 20 380 38 C240 56 110 30 0 44 Z" fill="var(--lime)"/>
    <path d="M0 44 C110 30 240 56 380 38 C520 20 640 70 780 40 V54 C640 84 520 34 380 52 C240 70 110 44 0 58 Z" fill="var(--lime-light)"/>
  </svg>

  <span class="dot dot--ring" style="left:440px;top:-8px;width:44px;height:44px;background:#fff"></span>
  <span class="dot" style="left:620px;top:40px;width:40px;height:40px"></span>
  <span class="dot" style="left:598px;top:60px;width:18px;height:18px"></span>
  <span class="dot" style="left:712px;top:30px;width:64px;height:64px"></span>
  <div class="bubble" style="left:357px;top:35px;width:110px;height:110px" role="img" aria-label="Photo of a happy jumping girl"></div>
  <div class="bubble" style="left:492px;top:44px;width:104px;height:104px" role="img" aria-label="Photo of a cheering child"></div>
  <div class="bubble" style="left:615px;top:26px;width:104px;height:104px" role="img" aria-label="Photo of a smiling boy"></div>

  <div class="col col--about">
    <h2>ABOUT US</h2>
    <p class="lead">Lorem ipsum dolor sit amet, consectetur adipisicing elit, sed do</p>
    <p class="body">Lorem ipsum dolor sit amet, consectetur adipisicing elit, sed do eiusmod tempor incididunt ut labore et dolore magna aliqua. Ut enim ad minim veniam, quis nostrud exercitation ullamco laboris nisi ut aliquip ex ea commodo consequat. Duis aute irure dolor in reprehenderit in voluptate velit esse cillum</p>
  </div>

  <div class="col col--services">
    <h2>SERVICES</h2>
    <p class="lead">Lorem ipsum dolor sit amet, consectetur adipisicing</p>
    <p class="body">Lorem ipsum dolor sit amet, consectetur adipisicing elit, sed do eiusmod tempor incididunt ut labore et dolore</p>
    <ul class="services-list">
      <li>Medical - Tallowby Family Health</li>
      <li>Tallowby Family Dental</li>
      <li>Physiotherapy (we say "Physio")</li>
      <li>Podiatry</li>
      <li>Psychology</li>
      <li>Dieticians</li>
    </ul>
  </div>

  <div class="col col--fees">
    <h2>FEE'S</h2>
    <p class="lead">Lorem ipsum dolor sit amet, consectetur adipisicing elit, sed do</p>
    <p class="body">Lorem ipsum dolor sit amet, consectetur adipisicing elit, sed do eiusmod tempor incididunt ut labore et dolore magna aliqua. Ut enim ad minim veniam, quis nostrud exercitation ullamco</p>
  </div>

  <div class="abs staff-photo" role="img" aria-label="Photo of the doctors and nursing staff in white coats"></div>
  <div class="abs group-photo" role="img" aria-label="Photo of a family smiling together"></div>
  <div class="abs couple-photo" role="img" aria-label="Photo of a smiling senior couple"></div>
</section>

</body>
</html>
```